Influencer agency website

K-Brightcast, Influencer Marketing Agency. A creative space where influencers and brands meet. We represent ideas and collaborations which bring marketing success to companies and brands.
Influencer types: Nano, Micro, Macro
Brand Types: Fashion, Beauty, Luxury Goods, Gaming, Sports, Home & Living, Travel, Lifestyle, Automotive

```html
<!DOCTYPE html>
<html lang="en">
<head>
<meta charset="utf-8">
<title>K-Brightcast — Influencer Marketing Agency</title>
<link href="https://fonts.googleapis.com/css2?family=Montserrat:wght@400;500;600;700&family=Raleway:wght@400;500;600&display=swap" rel="stylesheet">
<style>
:root{
  --black:#0b0b0b;
  --ink:#1d1714;
  --brown-dark:#4a3326;
  --brown:#6b5141;
  --brown-mid:#8c6f5c;
  --sand:#c9a992;
  --peach:#f1d6c3;
  --cream:#ece3dc;
  --white:#ffffff;
  --grey:#5d5d5d;
  --head:'Montserrat',sans-serif;
  --body:'Raleway',sans-serif;
}
*{box-sizing:border-box;margin:0;padding:0}
html,body{width:1200px;height:4705px;overflow:hidden}
body{position:relative;background:var(--white);font-family:var(--body);color:var(--ink)}
.abs{position:absolute}
.grad-text{background:linear-gradient(90deg,var(--brown-dark) 0%,var(--brown-dark) 45%,var(--sand) 70%,var(--peach) 100%);-webkit-background-clip:text;background-clip:text;color:transparent}

/* hero */
.hero{left:0;top:0;width:1200px;height:654px;background:var(--black);overflow:hidden}
.hero-photo{left:0;top:0;width:1200px;height:654px;background:
  linear-gradient(90deg,rgba(0,0,0,.92) 0%,rgba(0,0,0,.6) 35%,rgba(0,0,0,.15) 70%,rgba(0,0,0,.3) 100%),
  radial-gradient(ellipse at 75% 35%,#b89278 0%,#6b5242 35%,#2c221c 70%,#111 100%)}
.brand-mark{font-family:var(--head);font-weight:600;color:var(--peach);letter-spacing:1px}
.hero .brand-mark{left:155px;top:72px;font-size:22px}
.nav{left:447px;top:59px;display:flex;gap:24px;font-family:var(--head);font-size:13px;color:var(--white)}
.btn-contact{left:953px;top:44px;width:137px;height:47px;border:1px solid var(--white);color:var(--white);font-family:var(--head);font-weight:500;font-size:13px;display:flex;align-items:center;justify-content:center}
.social-side{left:34px;top:242px;display:flex;flex-direction:column;gap:24px}
.dot{width:9px;height:9px;border-radius:50%;background:var(--peach)}
.scroll-panel{left:0;top:438px;width:86px;height:216px;background:var(--white)}
.scroll-label{left:26px;top:520px;transform:rotate(-90deg);transform-origin:center;font-family:var(--head);font-size:9px;letter-spacing:1px;color:var(--ink);white-space:nowrap;width:80px;margin-left:-28px}
.scroll-knob{left:28px;top:576px;width:26px;height:26px;border-radius:50%;background:linear-gradient(135deg,var(--sand),var(--brown))}
.scroll-line{left:40px;top:596px;width:2px;height:12px;background:var(--ink)}
.hero-title{left:155px;top:240px;font-family:var(--head);font-weight:500;font-size:77px;line-height:70px;color:var(--white)}
.hero-title .accent{background:linear-gradient(90deg,#8a6b58,#d6b59f 60%,#f1d6c3);-webkit-background-clip:text;background-clip:text;color:transparent}
.btn-outline{border:1.5px solid var(--white);color:var(--white);font-family:var(--head);font-weight:600;font-size:13px;display:flex;align-items:center;justify-content:center;letter-spacing:.5px}
.hero .btn-outline{left:155px;top:500px;width:205px;height:46px}
.btn-arrow{left:349px;top:514px;width:20px;height:20px;background:var(--white)}

/* who */
.section-h{font-family:var(--head);font-weight:600;font-size:48px;letter-spacing:1px}
.who-h{left:137px;top:820px}
.who-text{left:137px;top:910px;width:370px;font-size:17.5px;line-height:24px;color:#333}
.who-text p+p{margin-top:24px}
.who-photo{left:548px;top:694px;width:602px;height:575px;background:radial-gradient(ellipse at 40% 45%,#e9d2c9 0%,#cdb6ad 30%,#efe6e1 60%,#fff 78%)}

/* services */
.services{left:86px;top:1287px;width:1028px;height:694px;background:linear-gradient(120deg,#5b4130 0%,#7a5e4c 35%,#b5988a 55%,#c7ae9f 68%,#a2826e 85%,#8a6a55 100%)}
.services-h{left:0;top:86px;width:1028px;text-align:center;background:linear-gradient(90deg,#d8c0b0 0%,#f1d6c3 45%,#fff 55%,#b89a86 100%);-webkit-background-clip:text;background-clip:text;color:transparent}
.svc{width:207px;height:197px;background:rgba(255,255,255,.22);display:flex;flex-direction:column;align-items:center;justify-content:flex-end;padding-bottom:38px}
.svc svg{width:62px;height:62px;margin-bottom:24px;fill:none;stroke:var(--white);stroke-width:2}
.svc span{font-family:var(--head);font-weight:600;font-size:17px;color:var(--white);letter-spacing:.5px}
.svc.active{background:var(--white)}
.svc.active svg{stroke:var(--sand)}
.svc.active span{color:var(--sand)}

/* trusted */
.trusted-h{left:155px;top:2044px;font-size:32px}
.partner{width:180px;text-align:center;font-family:var(--head);font-weight:600;font-size:24px;color:#8e8e8e}

/* band */
.band{left:0;top:2356px;width:1200px;height:464px;background:linear-gradient(90deg,#000 0%,#0d0d0d 55%,#3a3a3a 90%,#555 100%)}
.band-h{left:166px;top:90px;font-family:var(--head);font-weight:600;font-size:49px;line-height:57px;color:var(--white)}
.band .btn-outline{left:166px;top:348px;width:155px;height:46px;font-weight:500;font-size:12px}
.band-art{left:657px;top:18px;width:420px;height:402px;background:radial-gradient(ellipse at 50% 50%,#e8e8ea 0%,#a9a9ae 40%,rgba(60,60,60,.4) 70%,rgba(20,20,20,0) 80%)}

/* blog */
.blog-h{left:0;top:2925px;width:1200px;text-align:center}
.card{top:3015px;width:278px;height:473px;background:var(--cream);padding:13px}
.card-img{width:252px;height:149px}
.card .cat{margin-top:17px;font-family:var(--head);font-size:10.5px;color:#444;text-decoration:underline}
.card h3{margin-top:10px;font-family:var(--head);font-weight:600;font-size:14.5px;line-height:21px;color:var(--ink)}
.card .meta{margin-top:7px;font-family:var(--head);font-size:11.5px;color:#444}
.card .meta b{font-weight:600}
.card p.excerpt{margin-top:15px;font-size:14px;line-height:20.5px;color:#444}
.card .more{display:block;margin:20px auto 0;width:max-content;font-family:var(--head);font-weight:700;font-size:12px;color:var(--ink);border-bottom:1px solid var(--ink);padding-bottom:3px}
.card .more em{font-style:normal;color:var(--sand)}

/* clients */
.clients{left:0;top:3583px;width:1200px;height:708px;background:linear-gradient(180deg,#5a4333 0%,#5e4738 60%,#67503f 100%);overflow:hidden}
.clients-h{left:166px;top:72px;background:linear-gradient(90deg,#c9ab96,#f1d6c3 60%,#8c6f5c);-webkit-background-clip:text;background-clip:text;color:transparent}
.arrow-btn{width:90px;height:90px;border-radius:50%;border:2px solid rgba(255,255,255,.25);display:flex;align-items:center;justify-content:center}
.arrow-btn.on{border-color:var(--white)}
.arrow-btn svg{width:22px;height:22px;fill:none;stroke-width:2}
.client{width:265px;height:361px}
.client .who{position:absolute;left:16px;bottom:22px;display:flex;align-items:center;gap:12px;color:var(--white)}
.client .av{width:54px;height:54px;border-radius:50%;background:#e7d2c3;border:2px solid var(--white)}
.client .nm{font-family:var(--head);font-weight:500;font-size:16px}
.client .loc{font-family:var(--head);font-size:9px;margin-top:2px}

/* footer */
.footer-brand{left:55px;top:4470px;font-size:26px;color:var(--brown)}
.subscribe{left:298px;top:4362px;width:604px;height:44px;display:flex}
.subscribe .field{flex:1;background:var(--cream);border:1px solid #bbb;display:flex;align-items:center;padding-left:14px;gap:10px;font-family:var(--head);font-size:13px;color:#555}
.subscribe .join{width:131px;background:linear-gradient(90deg,#2a1d16,#6b5141 55%,#f1d6c3);color:var(--white);font-family:var(--head);font-weight:600;font-size:12px;display:flex;align-items:center;justify-content:center}
.follow{left:0;top:4460px;width:1200px;text-align:center;font-family:var(--head);font-weight:500;font-size:22px;color:var(--ink)}
.follow-icons{left:538px;top:4512px;display:flex;gap:28px}
.follow-icons .dot{background:var(--sand);width:11px;height:11px}
.foot-nav{top:4568px;font-family:var(--head);font-size:13px;color:var(--ink)}
.rule{left:124px;top:4636px;width:953px;height:1px;background:#bbb}
.copy{left:0;top:4663px;width:1200px;text-align:center;font-family:var(--head);font-size:12px;color:#444}
.copy span{color:var(--sand)}
</style>
</head>
<body>

<header class="abs hero">
  <div class="abs hero-photo" role="img" aria-label="Group of young creators laughing around a table while filming content with phones on tripods"></div>
  <div class="abs brand-mark">K-Brightcast</div>
  <nav class="abs nav"><span>Home</span><span>Who We Are</span><span>Our Services</span><span>Clients and Brands</span><span>Our Blog</span></nav>
  <div class="abs btn-contact">Contact Us</div>
  <div class="abs social-side"><div class="dot"></div><div class="dot"></div><div class="dot"></div><div class="dot"></div></div>
  <div class="abs scroll-panel"></div>
  <div class="abs scroll-label">SCROLL DOWN</div>
  <div class="abs scroll-knob"></div>
  <div class="abs scroll-line"></div>
  <h1 class="abs hero-title"><span class="accent">Influencer</span><br>Marketing<br>Agency</h1>
  <div class="abs btn-outline">FIND YOUR CALLING</div>
  <div class="abs btn-arrow"><svg viewBox="0 0 20 20" width="20" height="20"><path d="M8 6l4 4-4 4" fill="none" stroke="#1d1714" stroke-width="1.5"/></svg></div>
</header>

<section>
  <h2 class="abs section-h who-h grad-text">WHO WE ARE</h2>
  <div class="abs who-text">
    <p>Lorem ipsum dolor sit amet consectetur. Odio faucibus aliquet nullam nec proin egestas viverra. Aenean pulvinar risus eget sed justo sed non turpis aliquam. Duis felis in facilisis egestas purus platea interdum massa. Lorem nam gravida volutpat odio.</p>
    <p>Lorem ipsum dolor sit amet consectetur. Odio faucibus aliquet nullam nec proin egestas viverra.</p>
  </div>
  <div class="abs who-photo" role="img" aria-label="Young woman in a pink bucket hat and denim jacket adjusting sunglasses, headphones around her neck"></div>
</section>

<section class="abs services">
  <h2 class="abs section-h services-h">OUR SERVICES</h2>
  <div class="abs svc" style="left:69px;top:187px"><svg viewBox="0 0 62 62"><rect x="10" y="6" width="30" height="40"/><rect x="30" y="28" width="22" height="28"/><path d="M34 36h14M34 42h14M34 48h14"/></svg><span>SERVICE NAME</span></div>
  <div class="abs svc" style="left:297px;top:187px"><svg viewBox="0 0 62 62"><rect x="8" y="10" width="46" height="32"/><rect x="18" y="16" width="26" height="18"/><path d="M24 42v10M38 42v10M16 52h30"/></svg><span>SERVICE NAME</span></div>
  <div class="abs svc active" style="left:526px;top:187px"><svg viewBox="0 0 62 62"><rect x="14" y="18" width="14" height="24" rx="7"/><path d="M10 32a11 11 0 0 0 22 0M21 43v10M14 53h14"/><rect x="32" y="6" width="24" height="14" rx="3"/></svg><span>SERVICE NAME</span></div>
  <div class="abs svc" style="left:754px;top:187px"><svg viewBox="0 0 62 62"><rect x="6" y="8" width="50" height="42"/><path d="M6 16h50M14 42l10-10 8 6 14-14"/></svg><span>SERVICE NAME</span></div>
  <div class="abs svc" style="left:69px;top:406px"><svg viewBox="0 0 62 62"><path d="M20 56V44a18 18 0 1 1 22-6v4h-6v14"/><circle cx="30" cy="24" r="7"/></svg><span>SERVICE NAME</span></div>
  <div class="abs svc" style="left:297px;top:406px"><svg viewBox="0 0 62 62"><path d="M18 22l6 8 7-12 7 12 6-8-3 14H21z"/><path d="M6 46h10l10 4h16l12-8"/></svg><span>SERVICE NAME</span></div>
  <div class="abs svc" style="left:526px;top:406px"><svg viewBox="0 0 62 62"><path d="M14 40a10 10 0 0 1 2-20 14 14 0 0 1 27-2 11 11 0 0 1 3 22z"/><path d="M24 30l14-6v16l-14-6z"/></svg><span>SERVICE NAME</span></div>
  <div class="abs svc" style="left:754px;top:406px"><svg viewBox="0 0 62 62"><circle cx="31" cy="24" r="13"/><path d="M25 40h12M26 46h10M28 52h6M31 17v14"/></svg><span>SERVICE NAME</span></div>
</section>

<section>
  <h2 class="abs section-h trusted-h grad-text">WE ARE TRUSTED BY</h2>
  <div class="abs partner" style="left:113px;top:2140px">Starline Goods</div>
  <div class="abs partner" style="left:301px;top:2140px">Sweepo</div>
  <div class="abs partner" style="left:480px;top:2140px">Lensora</div>
  <div class="abs partner" style="left:681px;top:2140px">Rowan Athletic</div>
  <div class="abs partner" style="left:894px;top:2140px">Droplet</div>
  <div class="abs partner" style="left:113px;top:2228px">Alpine Kit</div>
  <div class="abs partner" style="left:301px;top:2228px">Homely</div>
  <div class="abs partner" style="left:480px;top:2228px">Tact</div>
  <div class="abs partner" style="left:681px;top:2228px">Mason Grove</div>
  <div class="abs partner" style="left:894px;top:2228px">Nutrimo</div>
</section>

<section class="abs band">
  <h2 class="abs band-h">WE CREATE<br>BRANDED<br>MARKETING<br>EXPERIENCES</h2>
  <div class="abs btn-outline">BOOK A CALL</div>
  <div class="abs band-art" role="img" aria-label="Dancer breaking out of a tilted live-stream phone screen with floating like icons and comment bubbles"></div>
</section>

<section>
  <h2 class="abs section-h blog-h grad-text">OUR INFLUENCER BLOG</h2>
  <article class="abs card" style="left:155px">
    <div class="card-img" role="img" aria-label="Smiling woman looking at her phone" style="background:linear-gradient(135deg,#3c3d3a,#c98e63 55%,#6b6a62)"></div>
    <div class="cat">UNCATEGORIZED</div>
    <h3>Lorem ipsum dolor sit amet consectetur.</h3>
    <div class="meta">By <b>Jonah M.</b> &nbsp;| &nbsp;January 27, 2023</div>
    <p class="excerpt">Lorem ipsum dolor sit amet consectetur. Odio faucibus aliquet nullam nec proin egestas viverra. Aenean pulvinar risus eget sed justo sed non turpis.</p>
    <span class="more">READ M<em>ORE</em></span>
  </article>
  <article class="abs card" style="left:456px">
    <div class="card-img" role="img" aria-label="Woman filming clothes with a phone on a tripod at a colourful table" style="background:linear-gradient(180deg,#eef0ee,#d6d9d4 55%,#c7b24f 75%,#6fae8d)"></div>
    <div class="cat">UNCATEGORIZED</div>
    <h3>Lorem ipsum dolor sit amet consectetur.</h3>
    <div class="meta">By <b>Jonah M.</b> January 27, 2023</div>
    <p class="excerpt">Lorem ipsum dolor sit amet consectetur. Odio faucibus aliquet nullam nec proin egestas viverra. Aenean pulvinar risus eget sed justo sed non turpis.</p>
    <span class="more">READ M<em>ORE</em></span>
  </article>
  <article class="abs card" style="left:767px">
    <div class="card-img" role="img" aria-label="Woman with phone surrounded by floating social reaction icons" style="background:linear-gradient(135deg,#dfe5ec,#c9d3dd 50%,#e7c9cf)"></div>
    <div class="cat">UNCATEGORIZED</div>
    <h3>Lorem ipsum dolor sit amet consectetur.</h3>
    <div class="meta">By <b>Jonah M.</b> &nbsp;| &nbsp;January 27, 2023</div>
    <p class="excerpt">Lorem ipsum dolor sit amet consectetur. Odio faucibus aliquet nullam nec proin egestas viverra. Aenean pulvinar risus eget sed justo sed non turpis.</p>
    <span class="more">READ M<em>ORE</em></span>
  </article>
</section>

<section class="abs clients">
  <h2 class="abs section-h clients-h">OUR CLIENTS</h2>
  <div class="abs arrow-btn" style="left:848px;top:61px"><svg viewBox="0 0 22 22" stroke="rgba(255,255,255,.3)"><path d="M14 4l-7 7 7 7"/></svg></div>
  <div class="abs arrow-btn on" style="left:954px;top:61px"><svg viewBox="0 0 22 22" stroke="#fff"><path d="M8 4l7 7-7 7"/></svg></div>

  <div class="abs client" style="left:-110px;top:292px" role="img" aria-label="Influencer in a magenta blazer posing in front of a building">
    <div style="position:absolute;inset:0;background:linear-gradient(180deg,#7f7a80,#a24c8c 60%,#5b3a55)"></div>
    <div class="who"><div class="av"></div><div><div class="nm">Bella Crane</div><div class="loc">USA</div></div></div>
  </div>
  <div class="abs client" style="left:188px;top:197px" role="img" aria-label="Influencer in a pink sweater taking a selfie against a yellow wall">
    <div style="position:absolute;inset:0;background:linear-gradient(180deg,#f2d21a,#e8c318 45%,#b8243f 75%,#3a2a12)"></div>
    <div class="who"><div class="av"></div><div><div class="nm">Carla Whitmore</div><div class="loc">USA</div></div></div>
  </div>
  <div class="abs client" style="left:486px;top:292px" role="img" aria-label="Young man taking a selfie in a city street">
    <div style="position:absolute;inset:0;background:linear-gradient(180deg,#7a8a92,#b7a79d 45%,#5d4a4a 80%,#2e2a2c)"></div>
    <div class="who"><div class="av"></div><div><div class="nm">Gus Harlan</div><div class="loc">USA</div></div></div>
  </div>
  <div class="abs client" style="left:793px;top:197px" role="img" aria-label="Woman in white sunglasses making an OK sign by the sea">
    <div style="position:absolute;inset:0;background:linear-gradient(180deg,#5c8fb3,#9bb8c9 40%,#d98aa9 70%,#8a2f69)"></div>
    <div class="who"><div class="av"></div><div><div class="nm">Bella Crane</div><div class="loc">USA</div></div></div>
  </div>
  <div class="abs client" style="left:1090px;top:292px" role="img" aria-label="Influencer in a magenta blazer holding a phone">
    <div style="position:absolute;inset:0;background:linear-gradient(180deg,#7f7a80,#a24c8c 60%,#5b3a55)"></div>
    <div class="who"><div class="av"></div><div><div class="nm">Daria Moss</div><div class="loc">USA</div></div></div>
  </div>
</section>

<footer>
  <div class="abs brand-mark footer-brand">K-Brightcast</div>
  <div class="abs subscribe">
    <div class="field"><svg width="14" height="11" viewBox="0 0 14 11"><rect x="0.5" y="0.5" width="13" height="10" fill="none" stroke="#777"/><path d="M1 1l6 5 6-5" fill="none" stroke="#777"/></svg>Email Address</div>
    <div class="join">JOIN NOW</div>
  </div>
  <div class="abs follow">Follow us on:</div>
  <div class="abs follow-icons"><div class="dot"></div><div class="dot"></div><div class="dot"></div><div class="dot"></div></div>
  <span class="abs foot-nav" style="left:243px">Home</span>
  <span class="abs foot-nav" style="left:333px">Who We Are</span>
  <span class="abs foot-nav" style="left:463px">Our Services</span>
  <span class="abs foot-nav" style="left:598px">Clients and Brands</span>
  <span class="abs foot-nav" style="left:774px">Our Blog</span>
  <span class="abs foot-nav" style="left:882px">Contact Us</span>
  <div class="abs rule"></div>
  <div class="abs copy">©Copyright 2023. <span>K-Brightcast</span> | All Rights Reserved</div>
</footer>

</body>
</html>
```